Brivora Collective Business Card Design

We need a business card design for Brivora Collective. We are a healthcare recruiting, wellness and education company. We partner with medical facilities to find quality candidates. We also offer free wellness courses.
The final design should communicate an emphasis on recruiting and wellness
The main purpose of the business card is to utilized it for networking events, give to hospitals, executives, VCs surgery centers and clinics. I want it to be sleek, clean, use of our brand colors and professional.

```html
<!DOCTYPE html>
<html lang="en">
<head>
<meta charset="utf-8">
<title>Brivora Collective Business Card</title>
<link rel="stylesheet" href="https://fonts.googleapis.com/css2?family=PT+Sans:wght@400;700&display=swap">
<style>
  :root {
    --bg-teal: #10b8ae;
    --bg-grey: #e5e5e5;
    --card-teal: #077a70;
    --card-deep: #025d56;
    --card-white: #ffffff;
    --ink-light: #ffffff;
  }
  * { margin: 0; padding: 0; box-sizing: border-box; }
  html, body { width: 1200px; height: 1200px; overflow: hidden; }
  body {
    position: relative;
    background: linear-gradient(to right, var(--bg-teal) 0 612px, var(--bg-grey) 612px 100%);
    font-family: "PT Sans", sans-serif;
    color: var(--ink-light);
  }
  .card {
    position: absolute;
    left: 229px;
    width: 805px;
    height: 460px;
    overflow: hidden;
  }
  .card--front { top: 101px; background: var(--card-white); }
  .card--back { top: 632px; background: var(--card-deep); }
  .card__shapes { position: absolute; inset: 0; width: 805px; height: 460px; }

  .identity { position: absolute; left: 30px; top: 96px; }
  .identity__icon { position: absolute; left: 0; top: 5px; width: 32px; height: 38px; }
  .identity__name {
    position: absolute; left: 41px; top: 0;
    font-weight: 700; font-size: 47px; line-height: 1; white-space: nowrap; letter-spacing: 0.5px;
  }
  .identity__role {
    position: absolute; left: 42px; top: 45px;
    font-size: 29px; line-height: 1; white-space: nowrap;
  }

  .contact { position: absolute; left: 28px; }
  .contact__icon { position: absolute; left: 0; top: 0; width: 38px; height: 40px; }
  .contact__text {
    position: absolute; font-size: 17px; line-height: 22px; white-space: nowrap; letter-spacing: 0.6px;
  }
  .contact--phone { top: 275px; }
  .contact--phone .contact__text { left: 48px; top: 0; letter-spacing: 1.4px; line-height: 19px; }
  .contact--mail { top: 334px; }
  .contact--mail .contact__text { left: 44px; top: -5px; }
  .contact--place { top: 393px; }
  .contact--place .contact__text { left: 44px; top: -5px; }

  .brand { position: absolute; text-align: center; font-weight: 400; color: var(--ink-light); }
  .brand__mark { display: block; margin: 0 auto 14px; width: 46px; height: 46px; background: var(--ink-light); border-radius: 6px; }
  .brand__name { display: block; font-size: 46px; line-height: 1; }
  .brand__sub { display: block; font-size: 27px; line-height: 1; margin-top: 2px; }
  .card--front .brand { left: 565px; top: 66px; width: 240px; }
  .card--back .brand { left: 540px; top: 266px; width: 240px; }

  .card__pattern {
    position: absolute; inset: 0;
    background: linear-gradient(135deg, #04665e 0%, var(--card-deep) 55%, #045f58 100%);
  }
</style>
</head>
<body>

  <section class="card card--front" aria-label="Business card front">
    <svg class="card__shapes" viewBox="0 0 805 460" aria-hidden="true">
      <path d="M0 0 H219 C362 50 472 190 472 350 C472 390 467 425 458 460 H0 Z" fill="var(--card-teal)"/>
      <path d="M501 0 H805 V366 C620 330 505 185 501 0 Z" fill="var(--card-deep)"/>
    </svg>

    <div class="identity">
      <svg class="identity__icon" viewBox="0 0 32 38" aria-hidden="true">
        <circle cx="16" cy="9" r="9" fill="#fff"/>
        <path d="M6 20 Q16 27 26 20 Q32 25 32 30 Q30 38 16 38 Q2 38 0 30 Q0 25 6 20 Z" fill="#fff"/>
      </svg>
      <div class="identity__name">YOUR NAME</div>
      <div class="identity__role">Your Position</div>
    </div>

    <div class="contact contact--phone">
      <svg class="contact__icon" viewBox="0 0 38 40" aria-hidden="true">
        <g stroke="#fff" stroke-width="1.4" fill="#fff">
          <line x1="3" y1="2" x2="3" y2="38"/><circle cx="3" cy="2" r="2"/>
          <line x1="33" y1="2" x2="33" y2="38"/><circle cx="33" cy="38" r="2"/>
        </g>
        <path d="M11 11 Q9 14 12 20 Q16 26 22 27 L24 25 L21 21 L19 22 Q15 19 14 15 L15 13 L12 10 Z" fill="#fff"/>
      </svg>
      <div class="contact__text">000 000 00000<br>000 000 00000</div>
    </div>

    <div class="contact contact--mail">
      <svg class="contact__icon" viewBox="0 0 38 40" aria-hidden="true">
        <g stroke="#fff" stroke-width="1.4" fill="#fff">
          <line x1="3" y1="2" x2="3" y2="38"/><circle cx="3" cy="2" r="2"/>
          <line x1="33" y1="2" x2="33" y2="38"/><circle cx="33" cy="38" r="2"/>
        </g>
        <rect x="8" y="13" width="20" height="13" fill="#fff"/>
        <path d="M8 13 L18 21 L28 13 M8 26 L15 19 M28 26 L21 19" stroke="var(--card-teal)" stroke-width="1" fill="none"/>
      </svg>
      <div class="contact__text">wwwyourmail@.com<br>wwwyourwebsite.com</div>
    </div>

    <div class="contact contact--place">
      <svg class="contact__icon" viewBox="0 0 38 40" aria-hidden="true">
        <g stroke="#fff" stroke-width="1.4" fill="#fff">
          <line x1="3" y1="2" x2="3" y2="38"/><circle cx="3" cy="2" r="2"/>
          <line x1="33" y1="2" x2="33" y2="38"/><circle cx="33" cy="38" r="2"/>
        </g>
        <path d="M18 6 C11 6 8 11 8 15 C8 20 14 26 18 31 C22 26 28 20 28 15 C28 11 25 6 18 6 Z" fill="#fff"/>
        <circle cx="18" cy="15" r="3.2" fill="var(--card-teal)"/>
        <circle cx="18" cy="15" r="1.6" fill="#fff"/>
      </svg>
      <div class="contact__text">Your Street, Your City<br>Your State, Your Country</div>
    </div>

    <div class="brand">
      <span class="brand__mark"></span>
      <span class="brand__name">Brivora</span>
      <span class="brand__sub">collective</span>
    </div>
  </section>

  <section class="card card--back" aria-label="Business card back">
    <div class="card__pattern" role="img" aria-label="Subtle repeating brand pattern in deep teal tones"></div>
    <div class="brand">
      <span class="brand__mark"></span>
      <span class="brand__name">Brivora</span>
      <span class="brand__sub">collective</span>
    </div>
  </section>

</body>
</html>
```